KRT business cards

I need a Business card design for my self. I am behavior analyst owner of a new company based in Miami. We offer Applied Behavior Analysis (ABA) services to individuals with developmental disabilities.

Business

```html
<!DOCTYPE html>
<html lang="en">
<head>
<meta charset="utf-8">
<title>KRT Business Cards</title>
<link href="https://fonts.googleapis.com/css2?family=Questrial&display=swap" rel="stylesheet">
<style>
  :root {
    --page-bg: #d9d6d2;
    --card-bg: #f2f2f2;
    --brand-blue: #135c96;
    --brand-green: #55a33f;
    --text-dark: #555a5e;
    --text-muted: #6d7175;
    --card-shadow: rgba(0, 0, 0, 0.22);
  }
  * { margin: 0; padding: 0; box-sizing: border-box; }
  html, body {
    width: 1200px;
    height: 900px;
    overflow: hidden;
    background: var(--page-bg);
    font-family: "Questrial", "Century Gothic", sans-serif;
  }
  .sheet {
    position: relative;
    width: 1200px;
    height: 900px;
  }
  .card {
    position: absolute;
    left: 320px;
    width: 560px;
    height: 320px;
    background: var(--card-bg);
    border-radius: 3px;
    box-shadow: 0 8px 22px var(--card-shadow);
    overflow: hidden;
  }
  .card--back { top: 110px; }
  .card--front { top: 470px; }
  .card__wave {
    position: absolute;
    inset: 0;
    width: 100%;
    height: 100%;
  }
  .wave__accent { fill: var(--brand-green); }
  .wave__band { fill: var(--brand-blue); }

  .brand {
    position: absolute;
    left: 64px;
    top: 52px;
    display: flex;
    align-items: center;
    gap: 8px;
  }
  .brand__dot {
    width: 16px;
    height: 16px;
    border-radius: 50%;
    background: var(--brand-green);
  }
  .brand__name {
    font-size: 38px;
    color: var(--brand-blue);
    letter-spacing: 2px;
    line-height: 1;
  }

  .services {
    position: absolute;
    left: 250px;
    top: 72px;
    list-style: none;
  }
  .services__item {
    display: flex;
    align-items: center;
    gap: 10px;
    font-size: 15px;
    color: var(--brand-blue);
    letter-spacing: 1px;
    line-height: 24px;
  }
  .services__tick {
    width: 12px;
    height: 12px;
    flex: none;
  }
  .services__tick path {
    fill: none;
    stroke: var(--brand-green);
    stroke-width: 2.4;
    stroke-linecap: round;
    stroke-linejoin: round;
  }

  .contact {
    position: absolute;
    left: 250px;
    top: 70px;
  }
  .contact__name {
    font-size: 20px;
    color: var(--text-dark);
    letter-spacing: 2px;
  }
  .contact__title {
    margin-top: 4px;
    font-size: 12.5px;
    color: var(--brand-green);
    letter-spacing: 1px;
  }
  .contact__lines {
    margin-top: 22px;
    list-style: none;
  }
  .contact__line {
    display: flex;
    align-items: center;
    gap: 12px;
    font-size: 13px;
    color: var(--text-muted);
    letter-spacing: 1px;
    line-height: 26px;
  }
  .contact__icon {
    width: 14px;
    height: 14px;
    flex: none;
  }
  .contact__icon * {
    fill: none;
    stroke: var(--brand-blue);
    stroke-width: 1.6;
    stroke-linejoin: round;
    stroke-linecap: round;
  }
</style>
</head>
<body>
<main class="sheet">

  <section class="card card--back" aria-label="Business card, services side">
    <svg class="card__wave" viewBox="0 0 560 320" preserveAspectRatio="none" aria-hidden="true">
      <path class="wave__accent" d="M0,140 C150,160 330,250 560,284 L560,320 L0,320 Z"/>
      <path class="wave__band" d="M0,150 C150,176 330,266 560,296 L560,320 L0,320 Z"/>
    </svg>
    <div class="brand">
      <span class="brand__dot"></span>
      <span class="brand__name">KRT</span>
    </div>
    <ul class="services">
      <li class="services__item">
        <svg class="services__tick" viewBox="0 0 12 12" aria-hidden="true"><path d="M2,6.5 L5,9.5 L10.5,2.5"/></svg>
        Applied Behavior Analysis
      </li>
      <li class="services__item">
        <svg class="services__tick" viewBox="0 0 12 12" aria-hidden="true"><path d="M2,6.5 L5,9.5 L10.5,2.5"/></svg>
        Parent/Teacher Training
      </li>
      <li class="services__item">
        <svg class="services__tick" viewBox="0 0 12 12" aria-hidden="true"><path d="M2,6.5 L5,9.5 L10.5,2.5"/></svg>
        Social Skills Training
      </li>
      <li class="services__item">
        <svg class="services__tick" viewBox="0 0 12 12" aria-hidden="true"><path d="M2,6.5 L5,9.5 L10.5,2.5"/></svg>
        Tutoring
      </li>
    </ul>
  </section>

  <section class="card card--front" aria-label="Business card, contact side">
    <svg class="card__wave" viewBox="0 0 560 320" preserveAspectRatio="none" aria-hidden="true">
      <path class="wave__accent" d="M0,140 C150,160 330,250 560,284 L560,320 L0,320 Z"/>
      <path class="wave__band" d="M0,150 C150,176 330,266 560,296 L560,320 L0,320 Z"/>
    </svg>
    <div class="brand">
      <span class="brand__dot"></span>
      <span class="brand__name">KRT</span>
    </div>
    <div class="contact">
      <p class="contact__name">Marisol Vega, B.A.</p>
      <p class="contact__title">Board Certified Asst. Behavior Analyst (BCABA)</p>
      <ul class="contact__lines">
        <li class="contact__line">
          <svg class="contact__icon" viewBox="0 0 14 14" aria-hidden="true">
            <path d="M3,1.5 L5.2,1.5 L6,4.5 L4.6,5.6 C5.4,7.4 6.6,8.6 8.4,9.4 L9.5,8 L12.5,8.8 L12.5,11 C12.5,11.8 11.8,12.5 11,12.5 C5.8,12.2 1.8,8.2 1.5,3 C1.5,2.2 2.2,1.5 3,1.5 Z"/>
          </svg>
          786-555-0142
        </li>
        <li class="contact__line">
          <svg class="contact__icon" viewBox="0 0 14 14" aria-hidden="true">
            <rect x="1.5" y="3" width="11" height="8"/>
            <path d="M1.5,3 L7,7.5 L12.5,3"/>
          </svg>
          vega.m.aba@mailbox.com
        </li>
      </ul>
    </div>
  </section>

</main>
</body>
</html>
```